Short film - Electronic Press Kit (EPK)

I need a electronic press kit document (A4 portrait) to promote a short film Lantern Gully. It will contain photographs, quotes, text. It should be eye-catching and interesting to look at. It is to promote my graduate film from film school. I have a copy of the film online so you can watch it or take screen grabs as needed. The press kit is highly likely to only be viewed digitally as a PDF. I would like the raw files so the text can be updated as needed e.g. if it gets into a festival. Ideally I would like to use the RALEWAY font and have included it in the uploads. I would like the design and tone of the press kit to reflect the film. I have included photographs n the draft of where I would like some to be placed but am open to suggestions of how to integrate more photographs in and make in more interesting.
Updates

Hi Designers,Please find text update attached Lantern Gully Draft Text V5-2. There have been minor text changes for the directors statement and the directors biography.There will not be any further changes to the text.Excited to see your designs!Thank you,Maud Added Sunday, May 29, 2016

Target Market(s)

It will be looked at by film festival selection committees.

Industry/Entity Type

Electronic

Requirements
Must have
• Please watch the film Lantern Gully https://clipvault.example/482615093 password harbor347
• I would like the tone and colours of the film to be reflected in the document.
• Ideally use of the Raleway font. Please use the photographs in the Lantern Press Kit document V3 as the minimum connected to the text. Please play around with the photo position, shape and how the information is displayed. I have included some quotes on the last that I'd like incorporated into earlier pages of the document in a larger font, can be on top of a photograph or not, as way of making them stand out when people skim read the document.
Nice to have
• I have uploaded lots more photographs that can be incorporated into the document as you see fit.

```html
<!DOCTYPE html>
<html lang="en">
<head>
<meta charset="utf-8">
<title>Lantern Gully – Directors Statement</title>
<link href="https://fonts.googleapis.com/css2?family=Raleway:ital,wght@0,300;0,400;0,500;1,300&display=swap" rel="stylesheet">
<style>
  :root {
    --ink: #000000;
    --paper: #ffffff;
    --accent: #d0202e;
    --highlight: #c8202c;
    --sky-top: #1d5f96;
    --sky-mid: #4f9fd2;
    --pool: #1a8fc4;
    --pool-deep: #0c5d8f;
  }
  * { margin: 0; padding: 0; box-sizing: border-box; }
  html, body {
    width: 848px;
    height: 1200px;
    overflow: hidden;
    background: var(--ink);
  }
  .page {
    position: relative;
    width: 848px;
    height: 1200px;
    background: var(--ink);
    font-family: "Raleway", sans-serif;
    color: var(--paper);
  }
  .hero-photo {
    position: absolute;
    left: 0; top: 0;
    width: 848px;
    height: 514px;
    background:
      linear-gradient(180deg, var(--sky-top) 0%, var(--sky-mid) 55%, #c9d3d2 66%, #6c8a8f 74%, var(--pool) 80%, var(--pool-deep) 100%);
  }
  .hero-quote {
    position: absolute;
    right: 56px;
    top: 52px;
    text-align: right;
  }
  .hero-quote__line {
    font-weight: 300;
    font-style: italic;
    font-size: 49px;
    line-height: 53px;
    letter-spacing: -0.5px;
  }
  .hero-quote__credit {
    margin-top: 8px;
    font-weight: 400;
    font-size: 24px;
  }
  .accent { color: var(--accent); }
  .statement {
    position: absolute;
    left: 35px;
    top: 556px;
    width: 765px;
  }
  .statement__title {
    font-weight: 400;
    font-size: 51px;
    letter-spacing: -1px;
    line-height: 60px;
    margin-bottom: 14px;
  }
  .statement p {
    font-size: 15.4px;
    line-height: 25.6px;
    text-align: justify;
    margin-bottom: 25.6px;
  }
  .statement p.statement__callout {
    text-align: left;
    margin-bottom: 26px;
  }
  .statement__callout span {
    background: var(--highlight);
    box-decoration-break: clone;
    -webkit-box-decoration-break: clone;
  }
  .statement__signature {
    position: absolute;
    right: 75px;
    top: 1066px;
    font-size: 15.4px;
    color: var(--accent);
  }
</style>
</head>
<body>
<main class="page">
  <div class="hero-photo" role="img" aria-label="Outdoor pool with a tall white diving tower, a diver standing on the ten-metre platform under a clear blue sky, pine trees and grandstands behind"></div>

  <blockquote class="hero-quote">
    <div class="hero-quote__line">Through simplicity,</div>
    <div class="hero-quote__line">there is poetry.</div>
    <div class="hero-quote__credit">Director <span class="accent">Maud Carrow</span></div>
  </blockquote>

  <section class="statement">
    <h1 class="statement__title"><span class="accent">Directors</span> Statement</h1>
    <p>Lantern Gully is a poetic exploration of the thought process involved in working through self-doubt, mentally preparing for action, and taking the final steps towards achieving a goal. It is played out in on the ten-metre dive platform, where failure can mean serious injury.</p>
    <p>I was drawn into the world of competitive diving by the strength and commitment it demands to succeed. Divers chase the elusive perfect score of ten.</p>
    <p class="statement__callout"><span>Perfectionism can be a strong and powerful motivator, but it can be paralyzing if the focus is too much on the outcome rather than the process. This is universal.</span><br><span>The film suggests that the final results matter less than the journey to get there.</span></p>
    <p>During my Masters studies at the Riverside College of the Arts, I have developed a strong understanding of visual storytelling. My philosophy of filmmaking is to explore my own darkest fears, bringing them into the light to share with an audience.</p>
    <p>By tapping into a raw truth, I believe these stories will always resonate with an audience. I have learnt through the process of making Lantern Gully that through simplicity, there is poetry.</p>
  </section>
  <div class="statement__signature">Maud Carrow</div>
</main>
</body>
</html>
```